Bright-Ladder Brochure

We would like a 3 panel layout format with copy on both sides and on each panel, (we will provide content).

We are Bright-Ladder and we work with business owners to achieve measurable growth and success based on 5 Core Pillars Of Momentum and (S.W.E) 60 Week Steady Whole Endeavour. We also work with the business leader and individuals within the organization with personal development.

We would like the brochure to have a corporate feel, but warm and inviting. We don't want a hard or aggressive feel.

We would like it to be available for pdf upload and physical print formats.

The winning design will also be invited to design a header for our website as well. The header will be consistent with the brochure, so please keep that in mind during your creative process.

I am enclosing a transparent copy of our company logo along with content for the brochure.

Thank you in advance for your consideration!

Gordon and Lorna
Updates

Sorry, but we forgot to include the front cover text.

It will read as follows,

Do you know the 5 Core Pillars Of Momentum  that are crucial to the success of any business today?

Also, please add the following to the back page

Website: www.bright-ladder-example.com
Resource Centre: www.blhubfiles-example.com 
Phone: +44 (0) 7700900417
Email: info@bright-ladder-example.com

Follow us on (please insert Facebook, Linkedin and YouTube logo)

I have uploaded a pdf format of brochure text.

Hello designers. I wanted to give some further input to help the process. Although the brochure is to target business, we don't want to over do it with corporate professioanls in all the photos. If there is an opportunity to incorporate photos of small business owners like, a butcher, baker, chef, flower shop etc. This would hopefully help us make an immpression to all small business owners.

Thank you, and good luck!

Gordon and Lorna  

Reason: A few designers have come come on board last minute. So I'd like to give everyone the same opportunity to respond. Sincerely, Gordon

Target Market(s)

Small Business Owners searching for new ways to grow their business in the UK and Republic Of Ireland.

Industry/Entity Type

Business

```html
<!DOCTYPE html>
<html lang="en">
<head>
<meta charset="utf-8">
<title>Bright-Ladder Brochure – Outside Spread</title>
<link rel="stylesheet" href="https://fonts.googleapis.com/css2?family=Roboto+Condensed:ital,wght@0,300;0,400;0,700;1,300&family=Open+Sans:wght@400;600&display=swap">
<style>
  :root {
    --backdrop: #e6e2de;
    --paper: #ffffff;
    --purple: #6a2877;
    --purple-soft: #a25aa9;
    --social-red: #c43a4a;
    --cream: #f5efc4;
    --grey-text: #5f5f5f;
    --grey-band: #7a7a7a;
    --body-text: #4a4a4a;
  }
  * { box-sizing: border-box; margin: 0; padding: 0; }
  html, body {
    width: 1200px; height: 960px; overflow: hidden;
    background: var(--backdrop);
  }
  .spread {
    position: absolute; left: 60px; top: 40px;
    width: 1080px; height: 880px;
    background: var(--paper);
    box-shadow: 0 6px 24px rgba(0,0,0,.18);
    overflow: hidden;
  }
  .panel { position: absolute; top: 0; height: 880px; width: 360px; }
  .panel--inside { left: 0; }
  .panel--back { left: 360px; }
  .panel--front { left: 720px; }
  .fold { position: absolute; top: 0; width: 1px; height: 880px; background: rgba(0,0,0,.06); }

  /* inside flap */
  .economy-title {
    position: absolute; left: 32px; top: 92px;
    font: 600 19px "Open Sans", sans-serif; color: var(--purple);
  }
  .economy-copy {
    position: absolute; left: 32px; top: 140px; width: 300px;
    font: 400 11px/1.45 "Open Sans", sans-serif; color: var(--body-text);
  }
  .jar-photo {
    position: absolute; left: 100px; top: 420px; width: 170px; height: 360px;
    border-radius: 40px 40px 28px 28px;
    background: linear-gradient(180deg, #4f8a2e 0%, #6aa23c 30%, #d9d9d6 42%, #a67c52 60%, #8a6240 100%);
  }

  /* shared photo across back + front */
  .hero { position: absolute; left: 360px; top: 0; width: 720px; height: 470px; }

  /* wordmark */
  .wordmark {
    position: absolute; display: flex; align-items: center; gap: 8px;
    font: 700 22px "Roboto Condensed", sans-serif; color: var(--purple);
    letter-spacing: .5px;
  }
  .wordmark__square { width: 16px; height: 16px; background: var(--grey-band); }
  .panel--back .wordmark { left: 100px; top: 500px; }
  .panel--front .wordmark { left: 34px; top: 508px; }

  .contact {
    position: absolute; left: 0; width: 360px; top: 588px; text-align: center;
    font: 300 15px/1.45 "Roboto Condensed", sans-serif; color: var(--grey-text);
  }
  .social {
    position: absolute; left: 0; width: 360px; top: 680px;
    display: flex; justify-content: center; gap: 10px;
    list-style: none;
  }
  .social__badge { width: 22px; height: 22px; border-radius: 3px; background: var(--purple-soft); }
  .social__badge--video { background: var(--social-red); }
  .tagline {
    position: absolute; left: 0; width: 360px; top: 790px; text-align: center;
    font: italic 300 22px "Roboto Condensed", sans-serif; color: var(--purple);
  }

  /* front cover */
  .cover-lead {
    position: absolute; left: 34px; top: 600px;
    font: 300 24px "Roboto Condensed", sans-serif; color: var(--purple-soft);
  }
  .cover-title {
    position: absolute; left: 34px; top: 632px; width: 310px;
    font: 700 42px/1.08 "Roboto Condensed", sans-serif; color: var(--purple);
    text-transform: uppercase; letter-spacing: -.3px;
  }
  .cover-sub {
    position: absolute; right: 24px; top: 740px; width: 300px; text-align: right;
    font: 400 17px/1.35 "Roboto Condensed", sans-serif; color: var(--grey-text);
  }

  .bottom-bands { position: absolute; left: 0; bottom: 0; width: 1080px; height: 40px; }
</style>
</head>
<body>
  <main class="spread">
    <section class="panel panel--inside">
      <h2 class="economy-title">The New Economy</h2>
      <p class="economy-copy">The UK economy is finally beginning to show signs of recovery, yet many may not realize that small to medium businesses generate half of the U.K.'s national income and 60% of all employment, so undoubtedly they are playing a major role in this “new economy” now emerging. Business is changing fast and it is more competitive than ever, so it is vital to the survival of any company, to find innovative and effective ways to attract new customers, keep them coming back and stay ahead of the competition.</p>
      <div class="jar-photo" role="img" aria-label="Young green plant growing from a glass jar filled with coins"></div>
    </section>

    <svg class="hero" viewBox="0 0 720 470">
      <defs>
        <linearGradient id="heroTones" x1="0" y1="0" x2="0" y2="1">
          <stop offset="0" stop-color="#dfe6e8"/>
          <stop offset=".25" stop-color="#b86a4e"/>
          <stop offset=".5" stop-color="#5d8f3a"/>
          <stop offset=".8" stop-color="#c24a3c"/>
          <stop offset="1" stop-color="#3f6a2c"/>
        </linearGradient>
      </defs>
      <path d="M0,0 H720 V470 Q540,450 360,440 Q180,430 0,418 Z" fill="var(--cream)"/>
      <path role="img" aria-label="Two smiling florists in aprons standing in a greenhouse full of hanging flower baskets" d="M24,0 H720 V448 Q540,428 360,418 Q180,408 24,396 Z" fill="url(#heroTones)"/>
    </svg>

    <section class="panel panel--back">
      <div class="wordmark"><span class="wordmark__square"></span>Bright-Ladder</div>
      <p class="contact">
        Website: www.bright-ladder-example.com<br>
        Phone: +44 (0) 7700900417<br>
        Email: info@bright-ladder-example.com
      </p>
      <ul class="social" aria-label="Follow us">
        <li class="social__badge social__badge--video" role="img" aria-label="Video channel link"></li>
        <li class="social__badge" role="img" aria-label="Social page link"></li>
        <li class="social__badge" role="img" aria-label="Professional network link"></li>
      </ul>
      <p class="tagline">LETS WORK TOGETHER</p>
    </section>

    <section class="panel panel--front">
      <div class="wordmark"><span class="wordmark__square"></span>Bright-Ladder</div>
      <p class="cover-lead">Do you know the</p>
      <h1 class="cover-title">5 Core Pillars<br>Of Momentum</h1>
      <p class="cover-sub">that are crucial to the success of any business today?</p>
    </section>

    <div class="fold" style="left:360px"></div>
    <div class="fold" style="left:720px"></div>

    <svg class="bottom-bands" viewBox="0 0 1080 40" preserveAspectRatio="none" aria-hidden="true">
      <path d="M0,14 Q360,24 720,26 V40 H0 Z" fill="var(--purple)"/>
      <path d="M0,30 Q360,36 720,36 L1080,30 V40 H0 Z" fill="var(--grey-band)"/>
    </svg>
  </main>
</body>
</html>
```